Luxury Photoalbum manufacturer needs banner design 8'x8'

We need a banner design for trade show purposes. We supply luxury one-of-a-kind photo albums to boudoir photographers. Our customers are female professional photographers - mostly in the age range of 26 - 40.Design needs to appeal to business women in this age range who see their business help empower women.Follow our website for our current look and feel. www.velvetkeepsake.com
It needs to be 8'x8'

Target Market(s)

Women professional boudoir photographers

Industry/Entity Type

Professional Photography

Font styles to use
Serif

Requirements
Must have
• Feminine but professional look and feel
• Need the LOGO to be very dominant
• Needs to be reasonably consistent with our website - www.velvetkeepsake.com
Nice to have
• Not necessary to use all the images - can use as few or many as makes sense.

```html
<!DOCTYPE html>
<html lang="en">
<head>
<meta charset="utf-8">
<title>Satin Memoir – Trade Show Banner</title>
<link rel="stylesheet" href="https://fonts.googleapis.com/css2?family=Cinzel:wght@500&family=Oswald:wght@600&family=Kaushan+Script&display=swap">
<style>
  :root {
    --brand-red: #c62232;
    --ink: #2b2b2b;
    --frame: #ffffff;
    --bg-light: #f5f5f7;
    --bg-mid: #d9dadf;
    --bg-damask: #c9cad0;
  }
  * { margin: 0; padding: 0; box-sizing: border-box; }
  html, body { width: 1200px; height: 1200px; overflow: hidden; }
  .banner {
    position: relative;
    width: 1200px;
    height: 1200px;
  }
  .damask-backdrop {
    position: absolute;
    inset: 0;
    background:
      radial-gradient(ellipse at 50% 48%, var(--bg-light) 0%, rgba(236,236,240,0.9) 45%, rgba(217,218,223,0.6) 100%),
      linear-gradient(135deg, var(--bg-damask) 0%, #e3e4e8 50%, var(--bg-damask) 100%);
  }
  .brand-name {
    position: absolute;
    left: 0; right: 0;
    top: 120px;
    text-align: center;
    font-family: "Cinzel", serif;
    font-weight: 500;
    color: var(--brand-red);
    font-size: 92px;
    line-height: 1;
    letter-spacing: 8px;
  }
  .brand-name span { display: block; }
  .brand-name span + span { margin-top: 40px; }
  .tagline {
    position: absolute;
    left: 0; right: 0;
    top: 428px;
    text-align: center;
    font-family: "Oswald", sans-serif;
    font-weight: 600;
    text-transform: uppercase;
    color: var(--ink);
    font-size: 50px;
    line-height: 70px;
  }
  .tagline .accent {
    font-family: "Kaushan Script", cursive;
    font-weight: 400;
    text-transform: none;
    color: var(--brand-red);
    font-size: 58px;
  }
  .album-grid { position: absolute; inset: 0; }
  .album-photo {
    position: absolute;
    width: 368px;
    height: 252px;
    border: 9px solid var(--frame);
  }
  .album-photo.velvet-stack { left: 211px; top: 572px; background: linear-gradient(160deg, #5a2b55 0%, #a4202e 40%, #5c5048 65%, #8e1a28 85%, #3a3030 100%); }
  .album-photo.pearl-stack  { left: 621px; top: 572px; background: linear-gradient(170deg, #a9a7a5 0%, #e8e6e3 40%, #c9c0c4 60%, #5e6378 85%, #8d8a86 100%); }
  .album-photo.silver-stack { left: 211px; top: 866px; background: linear-gradient(170deg, #2a2a2a 0%, #b9bbbd 35%, #8c8e91 55%, #3d3d3e 80%, #1e1e1f 100%); }
  .album-photo.sparkle-stack{ left: 621px; top: 866px; background: linear-gradient(170deg, #6d6a66 0%, #bfb39a 25%, #9c1b2b 45%, #1e2848 70%, #151515 100%); }
</style>
</head>
<body>
  <main class="banner">
    <div class="damask-backdrop" role="img" aria-label="Soft light grey damask wallpaper pattern"></div>

    <h1 class="brand-name">
      <span>Satin</span>
      <span>Memoir</span>
    </h1>

    <p class="tagline">
      <span class="accent">Time</span> is not measured by clock<br>
      but by <span class="accent">Moments...</span>
    </p>

    <section class="album-grid">
      <div class="album-photo velvet-stack" role="img" aria-label="Stack of velvet photo albums in purple, red and bronze with pearl strands"></div>
      <div class="album-photo pearl-stack" role="img" aria-label="White and slate blue albums tied with a pink satin ribbon and pearls"></div>
      <div class="album-photo silver-stack" role="img" aria-label="Stack of silver and black albums with satin ribbons"></div>
      <div class="album-photo sparkle-stack" role="img" aria-label="Glitter albums in gold, red, navy and black stacked on a table"></div>
    </section>
  </main>
</body>
</html>
```